Family Business Father/Son Consulting team needs a cover for their book on family workplace dynamics

We are a father/son consulting firm that focuses on the psychology of communication and performance in the workplace of financial advisors. We recently wrote a book on the topic of family members working in the same financial services practice together. So, we need someone to design the cover for our book. The book itself is in a self-help style with the occasional exercise. It is psychologically based and while specific to the finance industry, does not discuss finances itself.

We would like the cover to clearly communicate that this book is practical, easy to read, and impactful. The average reader is someone who is successful in business and work or will soon plan on working with a family member.

The Title is "The Steady Household Circle: Launching, Growing, and Handing Over a Kinship Enterprise in Wealth Advisory" by Owen Palvecki, RCC*TM(this should be a trademark) and Rob Palvecki, Ph.D. Foreword by Jan Morrell.

Target Market(s)

Financial advisors who work with family members. Usually it is a parent/child, but not always.

Industry/Entity Type

Consulting within Financial Services

Colors

Designer to choose colors to be used in the design.

Requirements
Must have
• The ability for the design to be a printed book and for E-book
Nice to have
• Could be a simple design with the title or with graphics,. We are open to either. Our business colors are in the royal blue range. So, that color scheme could be nice, but isn't essential if there is something more creative/better that you have in mind.
Should not have
• Extravagant/ too playful of colors, but can be fun with design

```html
<!DOCTYPE html>
<html lang="en">
<head>
<meta charset="utf-8">
<title>The Steady Household Circle — Book Cover</title>
<link href="https://fonts.googleapis.com/css2?family=Cinzel:wght@400;500&family=Crimson+Text:wght@400;600&display=swap" rel="stylesheet">
<style>
  :root {
    --page-bg: #ffffff;
    --sky-cream: #efe3cc;
    --sky-peach: #e9cfa6;
    --sky-haze: #d9d6c8;
    --horizon-gold: #f2c46a;
    --sea-teal: #2a7f9c;
    --deep-blue: #0f4f78;
    --ink-blue: #1d5a7c;
    --title-cream: #f6ecd6;
    --band-light: #f7e8c4;
    --band-gold: #ecd091;
  }
  * { margin: 0; padding: 0; box-sizing: border-box; }
  html, body {
    width: 1200px; height: 1106px; overflow: hidden;
    background: var(--page-bg);
  }
  .canvas {
    position: relative; width: 1200px; height: 1106px;
  }
  .cover {
    position: absolute; left: 330px; top: 43px;
    width: 540px; height: 1020px; overflow: hidden;
    background:
      linear-gradient(180deg,
        var(--sky-peach) 0%,
        var(--sky-cream) 22%,
        var(--sky-haze) 42%,
        var(--sky-cream) 50%,
        var(--horizon-gold) 54%,
        var(--sea-teal) 60%,
        var(--deep-blue) 100%);
    box-shadow: 0 6px 24px rgba(0,0,0,0.18);
  }
  .cover-scene {
    position: absolute; left: 0; top: 200px;
    width: 540px; height: 400px;
    background:
      radial-gradient(ellipse 60% 30% at 50% 78%, rgba(255,236,180,0.55), transparent 70%),
      linear-gradient(180deg, rgba(42,127,156,0) 0%, rgba(42,127,156,0.35) 70%, rgba(15,79,120,0.55) 100%);
  }
  .foreword {
    position: absolute; top: 60px; left: 0; width: 100%;
    text-align: center;
    font-family: "Crimson Text", serif; font-size: 23px;
    color: var(--ink-blue);
  }
  .title {
    position: absolute; top: 625px; left: 0; width: 100%;
    text-align: center;
    font-family: "Cinzel", serif; font-weight: 400;
    font-size: 42px; line-height: 1.2;
    color: var(--title-cream);
    text-shadow: 1px 2px 2px rgba(10,40,60,0.55);
  }
  .subtitle-band {
    position: absolute; top: 775px; left: 0; width: 100%; height: 84px;
    background: linear-gradient(90deg, var(--band-light) 0%, var(--band-gold) 100%);
    display: flex; align-items: center; justify-content: center;
    text-align: center;
    font-family: "Crimson Text", serif; font-size: 21px; line-height: 1.2;
    color: var(--ink-blue);
  }
  .authors {
    position: absolute; top: 905px; left: 0; width: 100%;
    text-align: center;
    font-family: "Crimson Text", serif; font-weight: 600;
    font-size: 19px; letter-spacing: 0.5px;
    color: var(--title-cream);
  }
</style>
</head>
<body>
<div class="canvas">
  <div class="cover">
    <div class="cover-scene" role="img" aria-label="Painted sunset scene of a family walking hand in hand in silhouette by the water"></div>
    <p class="foreword">Foreword by Jan Morrell</p>
    <h1 class="title">THE STEADY<br>HOUSEHOLD CIRCLE</h1>
    <p class="subtitle-band">Launching, Growing, and Handing Over a<br>Kinship Enterprise in Wealth Advisory</p>
    <p class="authors">OWEN PALVECKI, CKA &amp; ROB PALVECKI, PH.D.</p>
  </div>
</div>
</body>
</html>
```